Stationery Design Needed: Business Card, Letterhead, Folder Design

Logo files attached I plan on using the standard us folder size 9x12 as well as standard US business card and letter head. I am the owner of Meadowfall Restorative Spine Clinic, www.meadowfallspineclinic.example. I now have two locations, each with the same phone number and website. I enclosed my slogan and the information. I practice in an honest, ethical manor and place patients at a top priority. I want the designs to fit with my logo which symbolizes a blend of the symbol for ethical, honesty ( the peacock ) and the medusa ( medicine ) . I want to use the colors form my website blue, grey, silver to blend in and be cohesive and also match along the modern but natural colors along with blue and grey from the office. I want my cards and stationary to stand out

Target Market(s)

Lawyers, Surgeons, Primary Care Physicians Chiropractors

Industry/Entity Type

Business

Contact Information for Business Card

I want the cards and folders to stand out ...Bold colors I like the dark blue the best as I want this to be my signature color ...See below
I don t want too much white or too much aqua blue

Colors
3277b5

Requirements
Must have
• On Business cards... Must have logo, My name and practice, Two addresses, and my certifications from anesthesia and pain medicine .... web site easy to read for my target age audience 40 +
Nice to have
• slogan and other certifications
Should not have
• Confusing small to real letters ... so may need double sides but with all important on the front

```html
<!DOCTYPE html>
<html lang="en">
<head>
<meta charset="utf-8">
<title>Meadowfall Restorative Spine Clinic – Business Card</title>
<link href="https://fonts.googleapis.com/css2?family=Arimo:wght@400;700&display=swap" rel="stylesheet">
<style>
  :root {
    --backdrop: #2a2a2a;
    --card-white: #ffffff;
    --card-grey: #c8c9c9;
    --brand-blue: #1a8fcf;
    --text-light: #ffffff;
    --text-dark: #474747;
  }
  * { margin: 0; padding: 0; box-sizing: border-box; }
  html, body {
    width: 1200px; height: 987px; overflow: hidden;
    background: var(--backdrop);
    font-family: "Arimo", Arial, sans-serif;
  }
  .canvas { position: relative; width: 1200px; height: 987px; }
  .card {
    position: absolute; left: 293px; width: 615px; height: 351px; overflow: hidden;
  }
  .card-front { top: 130px; background: var(--card-white); }
  .card-back { top: 505px; background: var(--card-grey); }
  .front-swoosh { position: absolute; inset: 0; }

  .brand { position: absolute; display: flex; align-items: center; }
  .brand-dot { border-radius: 50%; background: var(--brand-blue); flex: none; }
  .brand-name {
    color: var(--brand-blue); font-weight: 700; line-height: 1.12; text-transform: uppercase;
  }
  .card-front .brand { left: 30px; top: 54px; gap: 12px; }
  .card-front .brand-dot { width: 44px; height: 44px; }
  .card-front .brand-name { font-size: 15px; width: 200px; }

  .details {
    position: absolute; right: 14px; top: 96px; text-align: right; color: var(--text-light);
  }
  .doctor-name { font-size: 21px; font-weight: 400; line-height: 24px; margin-bottom: 4px; }
  .credentials { list-style: none; font-size: 10px; font-weight: 700; line-height: 14px; }
  .address { font-size: 16px; line-height: 19px; margin-top: 7px; }
  .address + .address { margin-top: 6px; }
  .phone { font-size: 16px; line-height: 19px; margin-top: 6px; }

  .card-back .brand { left: 0; right: 0; top: 142px; justify-content: center; gap: 18px; }
  .card-back .brand-dot { width: 64px; height: 64px; }
  .card-back .brand-name { font-size: 22px; width: 260px; }
  .slogan {
    position: absolute; left: 0; right: 0; top: 297px; text-align: center;
    font-size: 15px; color: var(--text-dark);
  }
</style>
</head>
<body>
<main class="canvas">
  <section class="card card-front">
    <svg class="front-swoosh" width="615" height="351" viewBox="0 0 615 351" aria-hidden="true">
      <defs>
        <radialGradient id="panelGlow" cx="0.55" cy="0.6" r="0.75">
          <stop offset="0" stop-color="#24c0e0"/>
          <stop offset="1" stop-color="#1488c9"/>
        </radialGradient>
      </defs>
      <path d="M375 0 H615 V351 H118 C250 290 355 170 375 0 Z" fill="url(#panelGlow)"/>
      <path d="M335 100 C305 205 220 295 92 351 L112 351 C235 292 315 210 335 100 Z" fill="#1aa6dc"/>
    </svg>
    <div class="brand">
      <span class="brand-dot"></span>
      <span class="brand-name">Meadowfall Restorative Spine Clinic</span>
    </div>
    <div class="details">
      <h1 class="doctor-name">Daniel R. Whitcombe, D.O.</h1>
      <ul class="credentials">
        <li>Diplomat, Northgate Board of Pain Medicine</li>
        <li>Diplomat, Northgate Board of Anesthesiology</li>
        <li>Diplomat, Harlow Osteopathic Medical Examiners</li>
        <li>Adjunct Faculty Eastbrook College of</li>
        <li>Osteopathic Medicine, NBSPP Certified in Safe</li>
        <li>Controlled Substance Prescribing, NBSPP Certified</li>
        <li>in Fluoroscopy Reading &amp; Radiation Protection</li>
      </ul>
      <p class="address">4810 Harborview Ave<br>Westmere, N.J. 07050</p>
      <p class="address">2290 Route 9 West, Suite 110<br>Lindenfield, N.J., 07021-3316</p>
      <p class="phone">P: 555-014-2260 F: 555-014-2261</p>
    </div>
  </section>

  <section class="card card-back">
    <div class="brand">
      <span class="brand-dot"></span>
      <span class="brand-name">Meadowfall Restorative Spine Clinic</span>
    </div>
    <p class="slogan">Careful Treatment Built on Trust &amp; Skill</p>
  </section>
</main>
</body>
</html>
```